The Circle BOLQ: Global Policy to Local Action

We need two professional visuals that represent the vision and strategy of the organization. I attached two rough images of the first visual and one image of the second visual. I also attached a pdf of the narrative to give context for each visual.

Target Market(s)

Global Health Policy Makers

Colors
ec1f27

Requirements
Must have
• Two separate images representing the flow of the work

```html
<!DOCTYPE html>
<html lang="en">
<head>
<meta charset="utf-8">
<title>The Partnership Diagram – The Circle BOLQ</title>
<link href="https://fonts.googleapis.com/css2?family=Open+Sans:wght@400;700&family=Oswald:wght@300;400;600&display=swap" rel="stylesheet">
<style>
  :root{
    --brand-red:#ec1f27;
    --wedge-red:#d61f2c;
    --wedge-deep:#b81b2a;
    --ring-purple:#4f2a78;
    --ring-dark:#4a4a4a;
    --label-purple:#3b2a80;
    --ink:#2d2d2d;
    --white:#ffffff;
  }
  html,body{margin:0;padding:0;width:1200px;height:1153px;overflow:hidden;background:var(--white);}
  .diagram{display:block;width:1200px;height:1153px;}
  .title-arc{font-family:"Oswald",sans-serif;font-weight:600;font-size:30px;fill:var(--brand-red);letter-spacing:0.5px;}
  .pillar-label{font-family:"Oswald",sans-serif;font-weight:600;font-size:30px;fill:var(--white);}
  .goal-label{font-family:"Open Sans",sans-serif;font-size:13px;fill:var(--white);}
  .goal-label--small{font-size:12px;}
  .partner-label{font-family:"Open Sans",sans-serif;font-weight:700;font-size:16.5px;text-anchor:middle;}
  .partner-label--light{fill:var(--white);}
  .partner-label--dark{fill:var(--label-purple);}
  .brand-name{font-family:"Oswald",sans-serif;font-weight:400;font-size:24px;fill:var(--ink);letter-spacing:1px;text-anchor:middle;}
  .hub-caption{font-family:"Oswald",sans-serif;font-weight:300;font-size:21px;fill:var(--ink);text-anchor:middle;}
  .divider-pillar{stroke:var(--white);stroke-width:5;}
  .divider-goal{stroke:var(--white);stroke-width:2;}
  .divider-wedge{stroke:var(--white);stroke-width:3;}
</style>
</head>
<body>
<svg class="diagram" viewBox="0 0 1400 1345" xmlns="http://www.w3.org/2000/svg" role="img" aria-label="The Partnership Diagram: partners around a health system based on people's needs, framed by sustainable development goals">
  <defs>
    <radialGradient id="wedgeFill" cx="706" cy="672" r="310" gradientUnits="userSpaceOnUse">
      <stop offset="0.5" stop-color="var(--wedge-deep)"/>
      <stop offset="1" stop-color="var(--wedge-red)"/>
    </radialGradient>
    <linearGradient id="hubFill" x1="0" y1="0" x2="0" y2="1">
      <stop offset="0" stop-color="#ffffff"/>
      <stop offset="1" stop-color="#e4e4e6"/>
    </linearGradient>
    <filter id="hubShadow" x="-20%" y="-20%" width="140%" height="140%">
      <feDropShadow dx="0" dy="4" stdDeviation="6" flood-color="#000" flood-opacity="0.45"/>
    </filter>
    <path id="arcTop320" d="M428.9 512 A320 320 0 0 1 983.1 512"/>
    <path id="arcTop331" d="M419.3 506.5 A331 331 0 0 1 992.7 506.5"/>
    <path id="arcTop318" d="M430.6 513 A318 318 0 0 1 981.4 513"/>
    <path id="arcTop352" d="M401.2 496 A352 352 0 0 1 1010.8 496"/>
    <path id="arcTop405" d="M355.3 469.5 A405 405 0 0 1 1056.7 469.5"/>
    <path id="arcBot330" d="M420.2 837 A330 330 0 0 0 991.8 837"/>
    <path id="arcBot323" d="M426.3 833.5 A323 323 0 0 0 985.7 833.5"/>
    <path id="arcBot336" d="M415 840 A336 336 0 0 0 997 840"/>
    <path id="arcBot372" d="M383.8 858 A372 372 0 0 0 1028.2 858"/>
    <path id="arcBot425" d="M337.9 884.5 A425 425 0 0 0 1074.1 884.5"/>
  </defs>

  <!-- titles -->
  <text class="title-arc"><textPath href="#arcTop405" startOffset="50%" text-anchor="middle">THE PARTNERSHIP DIAGRAM</textPath></text>
  <text class="title-arc"><textPath href="#arcBot425" startOffset="50%" text-anchor="middle">SUSTAINABLE DEVELOPMENT GOALS</textPath></text>

  <!-- rings -->
  <circle class="ring-pillars" cx="706" cy="672" r="380" fill="var(--ring-dark)"/>
  <circle class="ring-goals" cx="706" cy="672" r="343" fill="var(--ring-purple)"/>
  <circle class="ring-partners" cx="706" cy="672" r="308" fill="url(#wedgeFill)"/>

  <!-- pillar dividers -->
  <g class="pillar-dividers">
    <line class="divider-pillar" x1="706" y1="288" x2="706" y2="329" transform="rotate(0 706 672)"/>
    <line class="divider-pillar" x1="706" y1="288" x2="706" y2="329" transform="rotate(97 706 672)"/>
    <line class="divider-pillar" x1="706" y1="288" x2="706" y2="329" transform="rotate(163 706 672)"/>
    <line class="divider-pillar" x1="706" y1="288" x2="706" y2="329" transform="rotate(231 706 672)"/>
    <line class="divider-pillar" x1="706" y1="288" x2="706" y2="329" transform="rotate(294 706 672)"/>
  </g>
  <circle cx="706" cy="672" r="343" fill="none" stroke="var(--white)" stroke-width="2"/>

  <!-- goal dividers -->
  <g class="goal-dividers">
    <line class="divider-goal" x1="706" y1="328" x2="706" y2="364" transform="rotate(0 706 672)"/>
    <line class="divider-goal" x1="706" y1="328" x2="706" y2="364" transform="rotate(32 706 672)"/>
    <line class="divider-goal" x1="706" y1="328" x2="706" y2="364" transform="rotate(64 706 672)"/>
    <line class="divider-goal" x1="706" y1="328" x2="706" y2="364" transform="rotate(97 706 672)"/>
    <line class="divider-goal" x1="706" y1="328" x2="706" y2="364" transform="rotate(128 706 672)"/>
    <line class="divider-goal" x1="706" y1="328" x2="706" y2="364" transform="rotate(163 706 672)"/>
    <line class="divider-goal" x1="706" y1="328" x2="706" y2="364" transform="rotate(196 706 672)"/>
    <line class="divider-goal" x1="706" y1="328" x2="706" y2="364" transform="rotate(230 706 672)"/>
    <line class="divider-goal" x1="706" y1="328" x2="706" y2="364" transform="rotate(262 706 672)"/>
    <line class="divider-goal" x1="706" y1="328" x2="706" y2="364" transform="rotate(294 706 672)"/>
    <line class="divider-goal" x1="706" y1="328" x2="706" y2="364" transform="rotate(325 706 672)"/>
  </g>
  <circle cx="706" cy="672" r="308" fill="none" stroke="var(--white)" stroke-width="2"/>

  <!-- wedge dividers -->
  <g class="wedge-dividers">
    <line class="divider-wedge" x1="706" y1="364" x2="706" y2="520" transform="rotate(0 706 672)"/>
    <line class="divider-wedge" x1="706" y1="364" x2="706" y2="520" transform="rotate(36 706 672)"/>
    <line class="divider-wedge" x1="706" y1="364" x2="706" y2="520" transform="rotate(72 706 672)"/>
    <line class="divider-wedge" x1="706" y1="364" x2="706" y2="520" transform="rotate(108 706 672)"/>
    <line class="divider-wedge" x1="706" y1="364" x2="706" y2="520" transform="rotate(144 706 672)"/>
    <line class="divider-wedge" x1="706" y1="364" x2="706" y2="520" transform="rotate(180 706 672)"/>
    <line class="divider-wedge" x1="706" y1="364" x2="706" y2="520" transform="rotate(216 706 672)"/>
    <line class="divider-wedge" x1="706" y1="364" x2="706" y2="520" transform="rotate(252 706 672)"/>
    <line class="divider-wedge" x1="706" y1="364" x2="706" y2="520" transform="rotate(288 706 672)"/>
    <line class="divider-wedge" x1="706" y1="364" x2="706" y2="520" transform="rotate(324 706 672)"/>
  </g>

  <!-- pillar labels -->
  <g class="pillar-labels">
    <g transform="rotate(-38 706 672)"><text class="pillar-label"><textPath href="#arcTop352" startOffset="50%" text-anchor="middle">ECONOMY</textPath></text></g>
    <g transform="rotate(43 706 672)"><text class="pillar-label"><textPath href="#arcTop352" startOffset="50%" text-anchor="middle">ENVIRONMENT</textPath></text></g>
    <g transform="rotate(-43 706 672)"><text class="pillar-label"><textPath href="#arcBot372" startOffset="50%" text-anchor="middle">INFRASTRUCTURE</textPath></text></g>
    <g transform="rotate(22 706 672)"><text class="pillar-label"><textPath href="#arcBot372" startOffset="50%" text-anchor="middle">PEOPLE</textPath></text></g>
    <g transform="rotate(-98 706 672)"><text class="pillar-label"><textPath href="#arcTop352" startOffset="50%" text-anchor="middle">SOCIETY</textPath></text></g>
  </g>

  <!-- goal labels -->
  <g class="goal-labels">
    <g transform="rotate(-17 706 672)"><text class="goal-label"><textPath href="#arcTop320" startOffset="50%" text-anchor="middle">Decent Work</textPath></text></g>
    <g transform="rotate(16 706 672)"><text class="goal-label"><textPath href="#arcTop320" startOffset="50%" text-anchor="middle">Affordable Clean Energy</textPath></text></g>
    <g transform="rotate(48 706 672)"><text class="goal-label"><textPath href="#arcTop320" startOffset="50%" text-anchor="middle">Availability of Healthy Food</textPath></text></g>
    <g transform="rotate(80 706 672)"><text class="goal-label"><textPath href="#arcTop320" startOffset="50%" text-anchor="middle">Clean Water &amp; Sanitation</textPath></text></g>
    <g transform="rotate(-68 706 672)">
      <text class="goal-label goal-label--small"><textPath href="#arcBot323" startOffset="50%" text-anchor="middle">Transportation for</textPath></text>
      <text class="goal-label goal-label--small"><textPath href="#arcBot336" startOffset="50%" text-anchor="middle">Accessibility</textPath></text>
    </g>
    <g transform="rotate(-35 706 672)"><text class="goal-label"><textPath href="#arcBot330" startOffset="50%" text-anchor="middle">Affordable &amp; Safe Housing</textPath></text></g>
    <g transform="rotate(0 706 672)"><text class="goal-label"><textPath href="#arcBot330" startOffset="50%" text-anchor="middle">Resilient Communities</textPath></text></g>
    <g transform="rotate(33 706 672)"><text class="goal-label"><textPath href="#arcBot330" startOffset="50%" text-anchor="middle">Recreational Opportunities</textPath></text></g>
    <g transform="rotate(66 706 672)"><text class="goal-label"><textPath href="#arcBot330" startOffset="50%" text-anchor="middle">Gender Equality</textPath></text></g>
    <g transform="rotate(-82 706 672)">
      <text class="goal-label goal-label--small"><textPath href="#arcTop331" startOffset="50%" text-anchor="middle">Quality Education &amp;</textPath></text>
      <text class="goal-label goal-label--small"><textPath href="#arcTop318" startOffset="50%" text-anchor="middle">Lifelong Learning</textPath></text>
    </g>
    <g transform="rotate(-50 706 672)"><text class="goal-label"><textPath href="#arcTop320" startOffset="50%" text-anchor="middle">Edequate Income</textPath></text></g>
  </g>

  <!-- partner labels -->
  <g class="partner-labels">
    <text class="partner-label partner-label--light" x="630" y="446">Political<tspan x="630" dy="21.5">Leadership</tspan></text>
    <text class="partner-label partner-label--dark" x="773" y="446">Policy<tspan x="773" dy="21.5">Making</tspan></text>
    <text class="partner-label partner-label--light" x="895" y="539">Health, Education<tspan x="895" dy="21.5">&amp; Labor Policy</tspan></text>
    <text class="partner-label partner-label--dark" x="938" y="668">Education &amp;<tspan x="938" dy="21.5">Research</tspan></text>
    <text class="partner-label partner-label--light" x="898" y="792">Social &amp;<tspan x="898" dy="21.5">Professional</tspan><tspan x="898" dy="21.5">Networks</tspan></text>
    <text class="partner-label partner-label--dark" x="779" y="884">Health<tspan x="779" dy="21.5">Workforce</tspan></text>
    <text class="partner-label partner-label--light" x="637" y="879">Community<tspan x="637" dy="21.5">Organization</tspan><tspan x="637" dy="21.5">&amp; Ownership</tspan></text>
    <text class="partner-label partner-label--dark" x="517" y="814">Community</text>
    <text class="partner-label partner-label--light" x="472" y="651">Social<tspan x="472" dy="21.5">Institutions &amp;</tspan><tspan x="472" dy="21.5">Business</tspan><tspan x="472" dy="21.5">Leadership</tspan></text>
    <text class="partner-label partner-label--dark" x="512" y="548">Management</text>
  </g>

  <!-- hub -->
  <g class="hub">
    <circle cx="706" cy="672" r="153" fill="url(#hubFill)" filter="url(#hubShadow)"/>
    <text class="brand-name" x="706" y="645">The Circle BOLQ</text>
    <text class="hub-caption" x="706" y="726">HEALTH SYSTEM BASED</text>
    <text class="hub-caption" x="706" y="753">ON PEOPLE’S NEEDS</text>
  </g>
</svg>
</body>
</html>
```